Flyer promoting Velmora's workshops and credentials

We run Training workshops for the data analyst community. We'd like a flyer to sell our services using a style and colour scheme consistent with our website www.velmoraskills.co.uk . I've attached some background info and some existing e-brochures for different workshops to give a flavour for content (but these are poorly designed and we don't want a similar design!!). There's also an overview document which gives more direction. The flyer will be sent with an accompanying letter to Learning & Development decision makers as well as Anlaytical team managers. It's purpose would be to generate enquiries and bookings for primarliy our flagship workshop 'Turning Figures Into Real Results'.

Target Market(s)

Learning and Development senior managers
Analytical team managers

Industry/Entity Type

Training

Font styles to use
Other font styles liked:
• Similar to website for consistency

Requirements
Must have
• Good copy! Slick design more in line with European (UK) style advertising rather than US.
Nice to have
• Some humour,
Should not have
• should not be as boring and non-sales based as the website!! Website is not a great example!

```html
<!DOCTYPE html>
<html lang="en">
<head>
<meta charset="utf-8">
<title>Velmora – Workshops for Data Analysts</title>
<link rel="stylesheet" href="https://fonts.googleapis.com/css2?family=Open+Sans:wght@400;600;700&display=swap">
<style>
:root{
  --navy:#1f2f7a;
  --orange:#f7892e;
  --orange-dark:#d96a1c;
  --blue:#2f52b9;
  --blue-deep:#2443a6;
  --ink:#1d1d1d;
  --footer:#141414;
  --stage:#e8e5e0;
  --teal-light:#a9d0e0;
  --teal-dark:#265f78;
}
*{margin:0;padding:0;box-sizing:border-box}
html,body{width:1200px;height:1121px;overflow:hidden;background:var(--stage);font-family:"Open Sans",Arial,sans-serif;color:var(--ink)}
.page{position:absolute;top:144px;width:558px;height:784px;background:#fff;box-shadow:0 4px 14px rgba(0,0,0,.35);overflow:hidden}
.page-front{left:26px}
.page-back{left:622px}
.masthead{position:absolute;left:0;top:0;width:100%;height:86px;background:#fff}
.brand{position:absolute;left:22px;top:22px;display:flex;align-items:center;gap:6px}
.brand-dot{width:14px;height:14px;border-radius:50%;background:var(--orange)}
.brand-name{font-size:31px;font-weight:700;color:var(--navy);line-height:1}
.brand-tag{position:absolute;left:70px;top:60px;font-size:10.5px;font-weight:700;color:var(--orange)}
.follow{position:absolute;left:458px;top:33px;width:82px;height:30px;border-radius:4px;background:#2ea4d8;color:#fff;font-size:7.5px;font-weight:700;text-align:center;line-height:1.2;padding-top:6px;text-transform:uppercase}
.hero{position:absolute;left:0;top:86px;width:100%;height:262px;background:var(--orange)}
.hero-title{position:absolute;left:22px;top:30px;font-size:39px;font-weight:700;color:#fff;line-height:47px}
.hero-strip{position:absolute;left:211px;top:0;width:15px;height:100%;background:var(--orange-dark);opacity:.35}
.hero-icon{position:absolute;left:226px;width:66px;height:62px;background:var(--blue-deep);display:flex;align-items:center;justify-content:center}
.hero-icon::before{content:"";position:absolute;left:-15px;top:0;width:15px;height:100%;background:var(--orange-dark)}
.hero-photo{position:absolute;left:292px;top:0;width:266px;height:100%;background:linear-gradient(135deg,#e9e4dc,#cfc4b4 45%,#8d8478)}
.overview{position:absolute;left:0;top:348px;width:100%;height:121px;background:linear-gradient(#e2e2e2,#fafafa);padding:10px 20px 0 20px}
h2{font-size:18px;font-weight:700;line-height:1.2;margin-bottom:4px}
.overview h2{color:var(--navy)}
p,li{font-size:9px;line-height:12px;text-align:justify}
.overview p{margin-bottom:8px}
.message{position:absolute;left:0;top:469px;width:100%;height:264px;background:linear-gradient(90deg,var(--blue-deep),#3b63d0);color:#fff;padding:12px 20px 0 20px}
.message p{margin-bottom:8px}
.points{list-style:none}
.points li{margin-bottom:4.5px;padding-left:9px;position:relative}
.points li::before{content:"-";position:absolute;left:0}
.subpoints{list-style:none;margin-left:58px;margin-top:10px}
.subpoints li{margin-bottom:4.5px;padding-left:18px;position:relative}
.subpoints li::before{content:"o";position:absolute;left:0}
.contact-bar{position:absolute;left:0;top:731px;width:100%;height:53px;background:var(--footer);border-top:3px solid #fff;display:flex;align-items:center;justify-content:space-between;padding:0 16px;color:var(--orange);font-size:12px}
.contact-bar span{display:flex;align-items:center;gap:6px}
.about{position:absolute;left:0;top:86px;width:100%;height:522px;background:linear-gradient(#d8d8d8,#fbfbfb 30%,#fff);padding:12px 20px 0 20px}
.about h2{color:var(--navy);font-size:16.5px;margin-bottom:2px}
.about p{font-size:8.6px;line-height:11.8px;margin-bottom:4px}
.challenges{list-style:none;margin-bottom:4px}
.challenges li{font-size:8.6px;line-height:11.8px;padding-left:17px;text-indent:-17px;margin-bottom:4.5px}
.audience{width:254px}
.audience p{text-align:left}
.skills-diagram{position:absolute;left:292px;top:330px;width:246px;height:176px;border-radius:3px;background:linear-gradient(var(--teal-light),var(--teal-dark))}
.testimonials{position:absolute;left:0;top:608px;width:100%;height:124px;background:linear-gradient(90deg,var(--blue-deep),#3b63d0);color:#fff;padding:10px 20px 0 20px}
.testimonials h2{font-size:16.5px}
.testimonials p{font-size:8.6px;line-height:11.8px;margin-bottom:5px}
</style>
</head>
<body>

<section class="page page-front">
  <header class="masthead">
    <div class="brand"><span class="brand-dot"></span><span class="brand-name">Velmora</span></div>
    <div class="brand-tag">Workshops for Data Analysts</div>
    <div class="follow">Follow us on<br>Chirpline</div>
  </header>

  <div class="hero">
    <h1 class="hero-title">Turning<br>Figures<br>Into Real<br>Results</h1>
    <div class="hero-strip"></div>
    <div class="hero-icon" style="top:18px">
      <svg width="44" height="30" viewBox="0 0 44 30" fill="#fff"><circle cx="10" cy="8" r="5"/><circle cx="34" cy="8" r="5"/><circle cx="22" cy="7" r="6"/><path d="M1 26c0-7 4-10 9-10s9 3 9 10zM25 26c0-7 4-10 9-10s9 3 9 10zM12 28c0-8 4-12 10-12s10 4 10 12z"/></svg>
    </div>
    <div class="hero-icon" style="top:98px">
      <svg width="46" height="42" viewBox="0 0 46 42" fill="none" stroke="#fff"><circle cx="17" cy="25" r="9" stroke-width="6" stroke-dasharray="4 3"/><circle cx="17" cy="25" r="4" stroke-width="3"/><circle cx="35" cy="12" r="6" stroke-width="4" stroke-dasharray="3 2"/><circle cx="36" cy="32" r="4" stroke-width="3" stroke-dasharray="2 2"/></svg>
    </div>
    <div class="hero-icon" style="top:186px">
      <svg width="46" height="42" viewBox="0 0 46 42" fill="#fff"><rect x="4" y="30" width="6" height="10"/><rect x="13" y="24" width="6" height="16"/><rect x="22" y="18" width="6" height="22"/><rect x="31" y="12" width="6" height="28"/><path d="M2 26 L30 6 L27 2 L42 2 L38 16 L35 12 L5 30z"/></svg>
    </div>
    <div class="hero-photo" role="img" aria-label="Photo of a team of colleagues gathered around a computer in a bright office"></div>
  </div>

  <section class="overview">
    <h2>Overview</h2>
    <p>A professional looking flyer in a similar style/colours to website pages. The flyer should be eye catching and yler will provide information about our approach experience and expertise , with a lot of testimonials and mainly focus on our flagship workshop (Turning Figures Into Real Results) with just a mention of the other workshops</p>
    <p>The flyer will be sent with an accompanying letter to Analytical team managers and Senior Learning &amp; Development people within medium/large organisations. The idea being if the letter gets separated from the flyer there’s enough enticement and information that anyone in the target audience seeing the flyer would be interested to investigate further.</p>
  </section>

  <section class="message">
    <h2>The Message</h2>
    <p>We want to be able to get across that these are essential development workshops for data analysts –only one of these workshops is around technical training, most of them are about how analysts need to behave, how to interact with their customers and present themselves and their work. Main messages that need to get across:-</p>
    <ul class="points">
      <li>Workshops developed by highly experienced practitioners</li>
      <li>Small audiences to keep interaction high and maximise learning experience.</li>
      <li>‘Turning Figures Into Real Results’ (flagship workshop) main selling points</li>
    </ul>
    <ul class="subpoints">
      <li>CPD accredited</li>
      <li>Unique</li>
      <li>99.4% of past attendees would recommend the workshop to other analysts</li>
      <li>Has plenty of positive testimonials</li>
      <li>Been attended by UK’s largest organisations (and regularly by some).</li>
      <li>Been running for over 10 years</li>
      <li>Cornerstone workshop in the development of analysts</li>
    </ul>
  </section>

  <footer class="contact-bar">
    <span><svg width="11" height="11" viewBox="0 0 12 12" fill="none" stroke="#fff" stroke-width="1.2"><circle cx="6" cy="6" r="5"/><path d="M1 6h10M6 1c-3 3-3 7 0 10M6 1c3 3 3 7 0 10"/></svg>www.velmoraskills.co.uk</span>
    <span><svg width="10" height="12" viewBox="0 0 10 12" fill="#fff"><path d="M2 0l2 3-1 2c1 2 2 3 3 4l2-1 2 2-1 2C4 12 0 6 0 2z"/></svg>0161 555 0148</span>
    <span><svg width="12" height="9" viewBox="0 0 12 9" fill="#fff"><path d="M0 0h12L6 5zM0 1.5l6 5 6-5V9H0z"/></svg>info@velmoraskills.co.uk</span>
  </footer>
</section>

<section class="page page-back">
  <header class="masthead">
    <div class="brand"><span class="brand-dot"></span><span class="brand-name">Velmora</span></div>
    <div class="brand-tag">Workshops for Data Analysts</div>
    <div class="follow">Follow us on<br>Chirpline</div>
  </header>

  <section class="about">
    <h2>About ‘Turning Figures Into Real Results’</h2>
    <p>This is my flagship 2 day workshop- if I get to speak to Analytical managers it’s usually a reasonably easy sell – it gives the analysts a number of practical steps and expected behaviours they can follow to ensure they deliver good analytical service whilst also improving their impact and increasing productivity by reducing re-work. Ultimately for any level of analyst it provides a template of standards to work to that will naturally help build credibility and trust with customers and enable them to work more proactively.at the end of the workshop they get checklist of behaviours and actions as an aide memoire – a few businesses have gone on to integrate this into their personal development review processes. There are a number of common issues/challenges analytical teams face and experience. These are :</p>
    <ol class="challenges">
      <li>1)&nbsp;&nbsp;&nbsp;They have (or rather take on) too much work (usually because they don’t plan effectively or they avoid negotiating deadlines ad say yes to everything).</li>
      <li>2)&nbsp;&nbsp;&nbsp;They work reactively and find no time to add value</li>
      <li>3)&nbsp;&nbsp;&nbsp;Their customers don’t involve them in the wider process and so they don’t feel they get the full picture and don’t get involved until last minute.</li>
      <li>4)&nbsp;&nbsp;&nbsp;They feel their customers don’t articulate themselves very well and are prone to changing their minds so they do lots of re-work.</li>
      <li>5)&nbsp;&nbsp;&nbsp;Their customers think that everything is just a press of a button whilst in reality it’s a lot more work than that.</li>
      <li>6)&nbsp;&nbsp;&nbsp;They struggle to get heard and suffer from a low profile within the business.</li>
      <li>7)&nbsp;&nbsp;&nbsp;They feel as though they spend a lot of time just turning the cog to spew out data.</li>
    </ol>
    <p>The workshop addresses all these challenges through sections dedicated to communication, planning and presenting data.</p>
    <p>I have lots of testimonials for the workshop and it’s now CPD accredited which is another reason why it’s a good lead product.</p>
    <p>I guess for the two audiences there are two hooks…</p>
    <div class="audience">
      <p>Training/HR – CPD accredited soft skills training specifically developed for data analysts, data scientists, Management Information and Business Intelligence professionals.</p>
      <p>Analytical Managers – Complementary soft skills training to help the analysts to become more proactive and customer orientated/consultative.</p>
      <p>I’ve developed a skills based triangle as a way of capturing the importance of soft skills to an analysts development (something totally lost on a significant portion of more technical orientated analysts)….</p>
      <p>Previous Marketing - This year I started to differentiate my marketing into prospects and customers whereas previously I sent everyone the same thing. So customers get updates and offers generally – prospects get a salesy email here are a few and their open/click rates.</p>
    </div>
    <div class="skills-diagram" role="img" aria-label="Skills triangle diagram showing soft skill levels across analyst roles"></div>
  </section>

  <section class="testimonials">
    <h2>Testimonials</h2>
    <p>We run a schedule of open public workshops as well as privately hosted workshops. We can also tailor the content to your specific requirement if necessary. So, whatever your budget we can usually deliver a programme that will fit your needs.</p>
    <p>Our current portfolio of workshops is provided overleaf but more detail and a list of currently scheduled open workshops can be found on the website at www.velmoraskills.co.uk.</p>
    <p>Any bookings made with reference to this flyer will benefit from a 10% discount on fees until February 18th 2016 (this may not be used in conjunction with any other promotional rates that may be available at the time of booking).</p>
  </section>

  <footer class="contact-bar">
    <span><svg width="11" height="11" viewBox="0 0 12 12" fill="none" stroke="#fff" stroke-width="1.2"><circle cx="6" cy="6" r="5"/><path d="M1 6h10M6 1c-3 3-3 7 0 10M6 1c3 3 3 7 0 10"/></svg>www.velmoraskills.co.uk</span>
    <span><svg width="10" height="12" viewBox="0 0 10 12" fill="#fff"><path d="M2 0l2 3-1 2c1 2 2 3 3 4l2-1 2 2-1 2C4 12 0 6 0 2z"/></svg>0161 555 0148</span>
    <span><svg width="12" height="9" viewBox="0 0 12 9" fill="#fff"><path d="M0 0h12L6 5zM0 1.5l6 5 6-5V9H0z"/></svg>info@velmoraskills.co.uk</span>
  </footer>
</section>

</body>
</html>
```